2in1 Bartender & Sommelier needs a business card

I need a business card. I worked as a bartender in many places but I just finished a sommelier school and I would like a new business card. I like minimal design, natural materials and something what makes the people think :) I try to be creative in cocktail making, like little mixology, little twist on recipes... I like to travel and discover new places, cultures and of course interesting drinks and improve continously...live a little bit crazy life. And I like what I do...

Target Market(s)

restaurant/winebar managers, winemakers, other sommeliers and bartenders, people who work in food and beverage sector

Industry/Entity Type

Hospitality

Contact Information for Business Card

Rozsa Tarkany
Bartender & Sommelier
Phone: (FR) +33 6 4827 3190
(HU) +36 70 918 6352

Font styles to use
Script

Requirements
Must have
• Some sign, I am a bartender and sommelier as well.
Nice to have
• black and white maybe with 1 or 2 extra color
Should not have
• very colourful, to many things on the card

```html
<!DOCTYPE html>
<html lang="en">
<head>
<meta charset="utf-8">
<title>Rozsa Tarkany – Bartender &amp; Sommelier</title>
<link rel="stylesheet" href="https://fonts.googleapis.com/css2?family=Kaushan+Script&display=swap">
<style>
  :root {
    --page: #ffffff;
    --card: #000000;
    --ink: #ffffff;
    --bottle-dark: #07060a;
    --bottle-amber: #3a2a12;
    --bottle-green: #0f2a1c;
    --bottle-blue: #141a3a;
    --bottle-wine: #3a0d16;
  }
  * { margin: 0; padding: 0; box-sizing: border-box; }
  html, body {
    width: 1200px;
    height: 864px;
    overflow: hidden;
    background: var(--page);
  }
  .business-card {
    position: absolute;
    left: 158px;
    top: 152px;
    width: 891px;
    height: 507px;
    background: var(--card);
    overflow: hidden;
    font-family: "Kaushan Script", cursive;
    color: var(--ink);
  }
  .bottle-shelf {
    position: absolute;
    left: 0;
    top: 142px;
    width: 100%;
    height: 256px;
    background:
      radial-gradient(ellipse 60px 120px at 8% 45%, var(--bottle-amber), transparent 70%),
      radial-gradient(ellipse 70px 130px at 22% 55%, var(--bottle-wine), transparent 70%),
      radial-gradient(ellipse 60px 120px at 38% 50%, var(--bottle-green), transparent 70%),
      radial-gradient(ellipse 70px 140px at 62% 55%, var(--bottle-amber), transparent 70%),
      radial-gradient(ellipse 80px 140px at 80% 50%, #3a3530, transparent 70%),
      radial-gradient(ellipse 60px 120px at 95% 45%, var(--bottle-blue), transparent 70%),
      linear-gradient(to bottom, #15120f, var(--bottle-dark));
  }
  .holder-name,
  .holder-role,
  .phone-line {
    position: absolute;
    left: 0;
    width: 100%;
    text-align: center;
    white-space: nowrap;
    line-height: 1;
    transform: translateY(-50%);
  }
  .holder-name {
    top: 90px;
    font-size: 88px;
    padding-left: 12px;
  }
  .holder-role {
    top: 190px;
    font-size: 62px;
    padding-left: 12px;
  }
  .phone-line {
    font-size: 36px;
  }
  .phone-fr { top: 424px; padding-left: 10px; }
  .phone-hu { top: 478px; padding-left: 0; }
  .phone-gap { display: inline-block; width: 18px; }
</style>
</head>
<body>
  <div class="business-card">
    <div class="bottle-shelf" role="img" aria-label="Dimly lit shelf of wine and spirit bottles, softly out of focus"></div>
    <h1 class="holder-name">Rozsa Tarkany</h1>
    <p class="holder-role">Bartender &amp; Sommelier</p>
    <p class="phone-line phone-fr">Phone: (FR)<span class="phone-gap"></span>+33 6 4827 3190</p>
    <p class="phone-line phone-hu">(HU)<span class="phone-gap"></span>+36 70 918 6352</p>
  </div>
</body>
</html>
```